R&T Builders and Spaces Business Card

We need to redesign our business card. We had used white vellum wih grey logo and txt in the past. I would like to bring a little life into our cards without being over the top. I think I will be going away from the vellum and printing soft touch business cards.
I have attached what we currently have and our new logo design.

```html
<!DOCTYPE html>
<html lang="en">
<head>
<meta charset="utf-8">
<title>R&amp;T Builders and Spaces — Business Card</title>
<link rel="stylesheet" href="https://fonts.googleapis.com/css2?family=Jost:wght@300;400;500;600&display=swap">
<style>
  :root {
    --backdrop: #252525;
    --card-white: #ffffff;
    --brand-grey: #737373;
    --ink: #111111;
    --muted: #8a8a8a;
    --address-grey: #6b6b6b;
  }
  * { box-sizing: border-box; margin: 0; padding: 0; }
  html, body {
    width: 1200px; height: 1200px; overflow: hidden;
    background: var(--backdrop);
    font-family: "Jost", "Futura", sans-serif;
  }
  .stage { position: relative; width: 1200px; height: 1200px; }

  .card {
    position: absolute; left: 200px; width: 746px; height: 435px;
    border-radius: 15px; overflow: hidden;
  }
  .card-front { top: 116px; background: var(--card-white); }
  .card-back { top: 621px; background: var(--brand-grey); }

  /* Brand lockup */
  .brand {
    position: absolute; left: 217px; top: 55px;
    display: flex; align-items: center; gap: 22px;
  }
  .brand-square { width: 55px; height: 55px; background: var(--brand-grey); }
  .brand-name {
    color: var(--ink); font-weight: 400; font-size: 25px;
    line-height: 27px; letter-spacing: 3px; text-transform: uppercase;
  }

  /* Person block */
  .person {
    position: absolute; right: 408px; top: 186px; text-align: right;
  }
  .person-name {
    font-size: 36px; font-weight: 500; letter-spacing: 2px;
    color: var(--ink); line-height: 40px;
  }
  .person-title {
    font-size: 11px; letter-spacing: 4px; color: var(--muted);
    text-transform: uppercase; margin-top: 2px;
  }
  .person-email { font-size: 20px; font-weight: 300; color: var(--ink); margin-top: 2px; }

  .divider {
    position: absolute; left: 372px; top: 200px;
    width: 2px; height: 106px; background: var(--ink);
  }

  .contact-list {
    position: absolute; left: 403px; top: 208px; list-style: none;
  }
  .contact-item {
    display: flex; align-items: center; gap: 12px;
    font-size: 25px; font-weight: 500; color: var(--ink); line-height: 28px;
  }
  .contact-icon { width: 16px; height: 18px; flex: none; fill: var(--ink); }

  .address {
    position: absolute; left: 0; right: 0; top: 375px; text-align: center;
    font-size: 19px; font-weight: 300; color: var(--address-grey);
  }

  .back-field { position: absolute; inset: 0; }
  .website {
    position: absolute; right: 47px; bottom: 48px;
    color: var(--card-white); font-size: 31px; line-height: 1;
  }
  .website-domain { font-weight: 600; }
  .website-tld { font-weight: 300; }
</style>
</head>
<body>
<main class="stage">
  <section class="card card-front" aria-label="Card front">
    <div class="brand">
      <div class="brand-square"></div>
      <div class="brand-name">R&amp;T Builders<br>and Spaces</div>
    </div>

    <div class="person">
      <div class="person-name">DANA MARLOW</div>
      <div class="person-title">/ Partner</div>
      <div class="person-email">danam@rtbuilders.com</div>
    </div>

    <div class="divider"></div>

    <ul class="contact-list">
      <li class="contact-item">
        <svg class="contact-icon" viewBox="0 0 16 18" aria-hidden="true"><path d="M3 2l3 0 1.5 4-2 1.3c.9 2 2.2 3.5 4.2 4.5L11 9.8l4 1.6V15c0 1-1 1.5-2 1.4C7 15.8 2.2 11 1.6 4.4 1.5 3 2 2 3 2z"/></svg>
        <span>555 014 2870</span>
      </li>
      <li class="contact-item">
        <svg class="contact-icon" viewBox="0 0 16 18" aria-hidden="true"><path d="M4 2h8v4H4zM1 7h14v7h-2v-3H3v3H1zM4 12h8v5H4z"/></svg>
        <span>555 014 2970</span>
      </li>
      <li class="contact-item">
        <svg class="contact-icon" viewBox="0 0 16 18" aria-hidden="true"><path d="M4.5 1h7a1.5 1.5 0 0 1 1.5 1.5v13a1.5 1.5 0 0 1-1.5 1.5h-7A1.5 1.5 0 0 1 3 15.5v-13A1.5 1.5 0 0 1 4.5 1zM5 3v10h6V3zm3 11a1 1 0 1 0 0 2 1 1 0 0 0 0-2z"/></svg>
        <span>555 017 4412</span>
      </li>
    </ul>

    <p class="address">410 W. Mesa Blvd., Suite 120, Tempe, AZ 85281</p>
  </section>

  <section class="card card-back" aria-label="Card back">
    <div class="back-field" role="img" aria-label="Large brand mark decoration in grey and white"></div>
    <p class="website"><span class="website-domain">rtbuilders</span><span class="website-tld">.com</span></p>
  </section>
</main>
</body>
</html>
```